A simple Chatterbook Ad (not Chatterbook Page) for weight loss surgery

It’s a simple ad in terms of the text.

The text should say:
Curious about weight loss surgery?
This 30 second quiz will tell you which procedure will suit you best

I'm open to variations in the text if it is thought to enhance the ad.

Targeted towards obese individuals who have been unable to lose weight with diet and exercise. My industry is weight loss surgery – webpage www.marcusbellweather.com.au. Clicking the ad leads to a quiz on my webpage relating to weight loss surgery. Most frequent users of this service are females (75%) between ages of 35 and 55 years.

Successful weight loss surgery can enable individuals who have been unable to lose weight to lose a substantial amount of the excess weight they are carrying to be healthier and happier.

```html
<!DOCTYPE html>
<html lang="en">
<head>
<meta charset="utf-8">
<title>Curious about weight loss surgery?</title>
<link rel="stylesheet" href="https://fonts.googleapis.com/css2?family=Montserrat:wght@400;500;700;800&display=swap">
<style>
  :root {
    --teal: #17968a;
    --grey: #6b6c70;
    --white: #ffffff;
    --skin: #e9c9b4;
    --top-teal: #2196b8;
    --denim-light: #8fb0d6;
    --denim: #5d86b8;
    --denim-dark: #44699c;
  }
  * { margin: 0; padding: 0; box-sizing: border-box; }
  html, body { width: 1200px; height: 1200px; overflow: hidden; background: var(--white); }
  .ad {
    position: relative;
    width: 1200px;
    height: 1200px;
    overflow: hidden;
    background: var(--white);
    font-family: "Montserrat", Arial, sans-serif;
  }
  .photo {
    position: absolute;
    left: 640px;
    top: 0;
    width: 560px;
    height: 1200px;
    background: linear-gradient(180deg, var(--top-teal) 0 11%, var(--skin) 14% 26%, var(--denim-light) 36%, var(--denim) 65%, var(--denim-dark) 100%);
    -webkit-mask-image: linear-gradient(90deg, transparent 0, #000 32%);
    mask-image: linear-gradient(90deg, transparent 0, #000 32%);
  }
  .headline { position: absolute; color: var(--teal); font-weight: 700; line-height: 1; white-space: nowrap; }
  .headline--curious { left: 66px; top: 84px; font-size: 100px; }
  .headline--weight { left: 138px; top: 186px; font-size: 84px; }
  .headline--surgery { left: 136px; top: 248px; font-size: 114px; }
  .about-tag {
    position: absolute;
    left: 67px;
    top: 206px;
    width: 47px;
    height: 150px;
    background: var(--grey);
    display: flex;
    align-items: center;
    justify-content: center;
  }
  .about-tag span {
    transform: rotate(-90deg);
    color: var(--white);
    font-weight: 700;
    font-size: 38px;
    line-height: 1;
  }
  .quiz { position: absolute; left: 66px; top: 522px; }
  .quiz__this { color: var(--teal); font-weight: 700; font-size: 88px; line-height: 1; }
  .quiz__number { color: var(--grey); font-weight: 700; font-size: 158px; line-height: 0.95; letter-spacing: -4px; margin-top: 6px; }
  .quiz__unit { color: var(--grey); font-weight: 700; font-size: 52px; line-height: 1.05; margin-top: -2px; }
  .quiz__promise { color: var(--teal); font-weight: 700; font-size: 53px; line-height: 1.03; white-space: nowrap; }
  .url-pill {
    position: absolute;
    left: 300px;
    top: 1072px;
    width: 640px;
    height: 59px;
    border-radius: 16px;
    background: var(--teal);
    color: var(--white);
    font-size: 35px;
    font-weight: 500;
    display: flex;
    align-items: center;
    justify-content: center;
    white-space: nowrap;
  }
  .brand {
    position: absolute;
    right: 30px;
    top: 34px;
    display: flex;
    align-items: center;
    gap: 10px;
    color: var(--white);
    font-weight: 500;
  }
  .brand__dot { width: 40px; height: 40px; border-radius: 50%; background: var(--white); }
  .brand__text { display: flex; flex-direction: column; line-height: 1.05; }
  .brand__name { font-size: 22px; letter-spacing: 0.5px; text-transform: uppercase; }
  .brand__role { font-size: 11px; letter-spacing: 0.6px; text-transform: uppercase; }
</style>
</head>
<body>
<div class="ad">
  <div class="photo" role="img" aria-label="Photo of a slim woman in a teal crop top holding out the waistband of oversized blue jeans"></div>

  <div class="headline headline--curious">Curious</div>
  <div class="about-tag"><span>about</span></div>
  <div class="headline headline--weight">weight loss</div>
  <div class="headline headline--surgery">surgery?</div>

  <div class="quiz">
    <div class="quiz__this">This</div>
    <div class="quiz__number">30</div>
    <div class="quiz__unit">second quiz</div>
    <div class="quiz__promise">will tell you which<br>procedure will suit<br>you best</div>
  </div>

  <div class="url-pill">www.marcusbellweather.com.au</div>

  <div class="brand">
    <div class="brand__dot"></div>
    <div class="brand__text">
      <span class="brand__name">Marcus Bellweather</span>
      <span class="brand__role">General, Upper GI &amp; Bariatric Surgeon</span>
    </div>
  </div>
</div>
</body>
</html>
```